Casas de Nueva Aurora Flyer

Make me a flyer postcard 5 x 7 horizontal, one sided. I want main title to be "Casas de Nueva Aurora". It needs to say “Familias que se forman en la fe y valores humanos, y trabajan para llevar a otras familias al encuentro con Cristo y la Virgen María.”  We are in 4 places, include this:
Reuniones Cada Domingo
Monte Tabor Alto, Falls Church: 11:15am - 301-555-0142
Luz Divina Norte, Sterling: 9:30am - 571-555-0187
Hogar Manassas Park, 9:45am - 703-555-0129
Paz Eterna Sur, Winchester: 2:30pm - 540-555-0163
Include the logo attached, and use the picture attached as the main image, you can select the people from the image only and delete background or keep background but make it fit in nicely to the postcard.

```html
<!DOCTYPE html>
<html lang="es">
<head>
<meta charset="utf-8">
<title>Casas de Nueva Aurora</title>
<link rel="stylesheet" href="https://fonts.googleapis.com/css2?family=Playfair+Display:wght@400;500&family=Sacramento&family=Poppins:wght@300;400&display=swap">
<style>
  :root {
    --page: #d9dadd;
    --cream: #fdf9f2;
    --cream-warm: #f9ead6;
    --gold: #a57a1e;
    --gold-light: #d2a84a;
    --gold-dark: #6e4d0e;
    --brown: #3a2414;
    --text: #3d3029;
  }
  * { margin: 0; padding: 0; box-sizing: border-box; }
  html, body {
    width: 1200px; height: 1200px; overflow: hidden;
    background: var(--page);
  }
  .postcard {
    position: absolute; left: 0; top: 171px;
    width: 1200px; height: 857px; overflow: hidden;
    background:
      radial-gradient(ellipse 60% 50% at 40% 60%, rgba(255,255,255,.9), transparent 70%),
      linear-gradient(160deg, var(--cream) 0%, #fcf3e6 55%, var(--cream-warm) 100%);
    font-family: "Poppins", sans-serif;
    color: var(--text);
  }
  .group-photo {
    position: absolute; left: 30px; top: 0; width: 800px; height: 350px;
    background: linear-gradient(180deg, #8fa47c 0%, #6f7f6a 30%, #7d7a98 60%, #b9a5a0 100%);
    -webkit-mask-image: radial-gradient(ellipse 55% 60% at 50% 45%, #000 55%, transparent 100%);
            mask-image: radial-gradient(ellipse 55% 60% at 50% 45%, #000 55%, transparent 100%);
    opacity: .85;
  }
  .dove-decoration {
    position: absolute; left: 930px; top: 400px; width: 260px; height: 260px;
    border-radius: 50%;
    background: radial-gradient(circle, rgba(246,214,150,.35), transparent 70%);
  }
  .gold-glow {
    position: absolute; left: 200px; top: 360px; width: 180px; height: 180px;
    border-radius: 50%;
    background: radial-gradient(circle, rgba(226,180,80,.3), transparent 70%);
  }
  .holy-family-icon { position: absolute; left: 916px; top: 44px; width: 242px; height: 340px; }
  .title-serif {
    position: absolute; left: 224px; top: 290px;
    font-family: "Playfair Display", serif; font-weight: 500;
    font-size: 92px; line-height: 1; letter-spacing: -5px;
    color: var(--gold);
    background: linear-gradient(180deg, var(--gold-light), var(--gold-dark));
    -webkit-background-clip: text; background-clip: text;
    -webkit-text-fill-color: transparent;
  }
  .title-script {
    position: absolute; left: 455px; top: 376px;
    font-family: "Sacramento", cursive;
    font-size: 98px; line-height: 1; color: var(--brown);
    white-space: nowrap;
  }
  .tagline {
    position: absolute; left: 0; width: 1200px; top: 530px;
    text-align: center; font-size: 21px; line-height: 29px; font-weight: 300;
  }
  .meetings-pill {
    position: absolute; left: 442px; top: 620px; width: 316px; height: 34px;
    border-radius: 17px;
    background: linear-gradient(180deg, var(--gold-light), var(--gold-dark));
    color: #fff; text-align: center;
    font-family: "Playfair Display", serif; font-size: 21px; line-height: 34px; letter-spacing: -.5px;
  }
  .locations { position: absolute; left: 0; top: 672px; width: 1200px; height: 150px; }
  .location { position: absolute; top: 0; }
  .location .time {
    font-family: "Playfair Display", serif; font-size: 52px; line-height: 56px;
    letter-spacing: -3px; font-variant-numeric: lining-nums;
    background: linear-gradient(180deg, var(--gold-light), var(--gold-dark));
    -webkit-background-clip: text; background-clip: text;
    -webkit-text-fill-color: transparent;
  }
  .location .line {
    display: flex; align-items: flex-start; gap: 5px;
    font-size: 21px; line-height: 28px; font-weight: 300; margin-left: 4px;
  }
  .location .line svg { flex: none; margin-top: 6px; }
  .location .line.phone svg { margin-top: 8px; }
  .divider { position: absolute; top: 5px; width: 1.5px; height: 138px; background: var(--gold); opacity: .7; }
</style>
</head>
<body>
<main class="postcard">
  <div class="group-photo" role="img" aria-label="Foto de grupo de familias al aire libre"></div>
  <div class="gold-glow"></div>
  <div class="dove-decoration" role="img" aria-label="Paloma decorativa en tono dorado suave"></div>

  <svg class="holy-family-icon" viewBox="0 0 241 340" role="img" aria-label="Icono religioso de la Sagrada Familia en marco dorado">
    <defs>
      <linearGradient id="frameGold" x1="0" y1="0" x2="1" y2="1">
        <stop offset="0" stop-color="#8a7338"/><stop offset=".5" stop-color="#5c4a22"/><stop offset="1" stop-color="#8a7338"/>
      </linearGradient>
      <linearGradient id="iconFill" x1="0" y1="0" x2="0" y2="1">
        <stop offset="0" stop-color="#c9a24a"/><stop offset=".35" stop-color="#b3241f"/><stop offset="1" stop-color="#8f1c18"/>
      </linearGradient>
    </defs>
    <polygon points="0,60 120,0 241,60 241,340 0,340" fill="url(#frameGold)"/>
    <polygon points="18,70 120,20 223,70 223,322 18,322" fill="url(#iconFill)"/>
  </svg>

  <h1 class="title-serif">Casas de</h1>
  <div class="title-script">Nueva Aurora</div>

  <p class="tagline">Familias que se forman en la fe y valores humanos, y trabajan para llevar<br>a otras familias al encuentro con Cristo y la Virgen María.</p>

  <div class="meetings-pill">Reuniones Cada Domingo</div>

  <section class="locations">
    <div class="location" style="left:42px">
      <div class="time">11:15am</div>
      <div class="line"><svg width="12" height="16" viewBox="0 0 12 16"><path d="M6 0a6 6 0 0 0-6 6c0 4.5 6 10 6 10s6-5.5 6-10a6 6 0 0 0-6-6zm0 8.5A2.5 2.5 0 1 1 6 3.5a2.5 2.5 0 0 1 0 5z" fill="var(--gold)"/></svg><span>Monte Tabor Alto,<br>Falls Church</span></div>
      <div class="line phone"><svg width="14" height="14" viewBox="0 0 24 24"><path d="M6.6 10.8a15 15 0 0 0 6.6 6.6l2.2-2.2c.3-.3.7-.4 1-.2 1.1.4 2.3.6 3.6.6.6 0 1 .4 1 1V20c0 .6-.4 1-1 1A17 17 0 0 1 3 4c0-.6.4-1 1-1h3.5c.6 0 1 .4 1 1 0 1.3.2 2.5.6 3.6.1.3 0 .7-.2 1z" fill="var(--gold)"/></svg><span>301-555-0142</span></div>
    </div>
    <div class="divider" style="left:290px"></div>
    <div class="location" style="left:332px">
      <div class="time">9:45am</div>
      <div class="line"><svg width="12" height="16" viewBox="0 0 12 16"><path d="M6 0a6 6 0 0 0-6 6c0 4.5 6 10 6 10s6-5.5 6-10a6 6 0 0 0-6-6zm0 8.5A2.5 2.5 0 1 1 6 3.5a2.5 2.5 0 0 1 0 5z" fill="var(--gold)"/></svg><span>Hogar<br>Manassas Park</span></div>
      <div class="line phone"><svg width="14" height="14" viewBox="0 0 24 24"><path d="M6.6 10.8a15 15 0 0 0 6.6 6.6l2.2-2.2c.3-.3.7-.4 1-.2 1.1.4 2.3.6 3.6.6.6 0 1 .4 1 1V20c0 .6-.4 1-1 1A17 17 0 0 1 3 4c0-.6.4-1 1-1h3.5c.6 0 1 .4 1 1 0 1.3.2 2.5.6 3.6.1.3 0 .7-.2 1z" fill="var(--gold)"/></svg><span>703-555-0129</span></div>
    </div>
    <div class="divider" style="left:580px"></div>
    <div class="location" style="left:622px">
      <div class="time">9:30am</div>
      <div class="line"><svg width="12" height="16" viewBox="0 0 12 16"><path d="M6 0a6 6 0 0 0-6 6c0 4.5 6 10 6 10s6-5.5 6-10a6 6 0 0 0-6-6zm0 8.5A2.5 2.5 0 1 1 6 3.5a2.5 2.5 0 0 1 0 5z" fill="var(--gold)"/></svg><span>Luz Divina Norte,<br>Sterling</span></div>
      <div class="line phone"><svg width="14" height="14" viewBox="0 0 24 24"><path d="M6.6 10.8a15 15 0 0 0 6.6 6.6l2.2-2.2c.3-.3.7-.4 1-.2 1.1.4 2.3.6 3.6.6.6 0 1 .4 1 1V20c0 .6-.4 1-1 1A17 17 0 0 1 3 4c0-.6.4-1 1-1h3.5c.6 0 1 .4 1 1 0 1.3.2 2.5.6 3.6.1.3 0 .7-.2 1z" fill="var(--gold)"/></svg><span>571-555-0187</span></div>
    </div>
    <div class="divider" style="left:879px"></div>
    <div class="location" style="left:922px">
      <div class="time">2:30pm</div>
      <div class="line"><svg width="12" height="16" viewBox="0 0 12 16"><path d="M6 0a6 6 0 0 0-6 6c0 4.5 6 10 6 10s6-5.5 6-10a6 6 0 0 0-6-6zm0 8.5A2.5 2.5 0 1 1 6 3.5a2.5 2.5 0 0 1 0 5z" fill="var(--gold)"/></svg><span>Paz Eterna Sur,<br>Winchester</span></div>
      <div class="line phone"><svg width="14" height="14" viewBox="0 0 24 24"><path d="M6.6 10.8a15 15 0 0 0 6.6 6.6l2.2-2.2c.3-.3.7-.4 1-.2 1.1.4 2.3.6 3.6.6.6 0 1 .4 1 1V20c0 .6-.4 1-1 1A17 17 0 0 1 3 4c0-.6.4-1 1-1h3.5c.6 0 1 .4 1 1 0 1.3.2 2.5.6 3.6.1.3 0 .7-.2 1z" fill="var(--gold)"/></svg><span>540-555-0163</span></div>
    </div>
  </section>
</main>
</body>
</html>
```